New Company Introduction

We have launched a new business channel and need an online 'brochure' that we can use to announce us. Short, no more than 5 pages, clean, simple and changeable as we develop. See our new website for direction www.skyvellomedlift.example the introduction is to be issued to insurance companies, government departments and private clinics

Industry/Entity Type

Government

Font styles to use
Sans Serif

```html
<!DOCTYPE html>
<html lang="en">
<head>
<meta charset="utf-8">
<title>Skyvello Medlift – About</title>
<link href="https://fonts.googleapis.com/css2?family=Roboto:wght@300;400&display=swap" rel="stylesheet">
<style>
  :root {
    --brand-blue: #1f6fb3;
    --brand-deep: #0a4f8c;
    --nav-top: #1c6fb5;
    --nav-bottom: #034a8a;
    --panel-light: #dce8f3;
    --panel-strip: #c9dced;
    --text-body: #3a3a3a;
    --white: #ffffff;
    --header-sky: #e6eff7;
    --header-steel: #b7cde0;
  }
  * { margin: 0; padding: 0; box-sizing: border-box; }
  html, body { width: 1200px; height: 927px; overflow: hidden; background: var(--white); }
  body { font-family: "Roboto", Arial, sans-serif; color: var(--text-body); }

  .page { position: relative; width: 1200px; height: 927px; overflow: hidden; }

  .hero {
    position: absolute; left: 0; top: 0; width: 1200px; height: 243px;
    background: linear-gradient(100deg, #ffffff 0%, var(--header-sky) 35%, var(--header-steel) 60%, #d9e6f1 80%, #eef4f9 100%);
  }
  .brand-mark {
    position: absolute; left: 48px; top: 42px; width: 150px; height: 150px;
    background: var(--brand-deep);
  }
  .brand-name {
    position: absolute; left: 215px; top: 78px;
    font-weight: 300; font-size: 51px; letter-spacing: 0.5px;
    color: var(--brand-blue); white-space: nowrap;
  }

  .main-nav {
    position: absolute; left: 77px; top: 243px; width: 1046px; height: 70px;
    background: linear-gradient(180deg, var(--nav-top) 0%, var(--nav-bottom) 100%);
    border-radius: 0 0 14px 14px;
    display: flex; align-items: center; justify-content: center;
    padding-top: 14px;
    color: var(--white); font-size: 22px; font-weight: 300; letter-spacing: 0.3px;
    white-space: nowrap;
  }
  .main-nav .sep { margin: 0 7px; opacity: 0.8; }

  .content-panel {
    position: absolute; left: 0; top: 313px; width: 615px; height: 502px;
    background: var(--panel-light);
  }
  .content-strip {
    position: absolute; left: 0; top: 0; width: 152px; height: 502px;
    background: var(--panel-strip);
  }

  .social-links { position: absolute; top: 346px; left: 920px; width: 192px; height: 30px; }
  .social-links span {
    position: absolute; top: 0; width: 30px; height: 30px; border-radius: 5px;
    background: linear-gradient(180deg, #5b8fc7, #2a64a8);
  }

  .page-title {
    position: absolute; left: 124px; top: 368px;
    font-weight: 300; font-size: 53px; color: var(--brand-blue); letter-spacing: 0.5px;
  }

  .column {
    position: absolute; top: 438px; width: 473px;
    font-size: 14px; line-height: 18.2px; text-align: justify;
  }
  .column p { margin-bottom: 18.2px; }
  .column-left { left: 126px; }
  .column-right { left: 633px; }

  .site-footer {
    position: absolute; left: 0; top: 815px; width: 1200px; height: 112px;
    background: linear-gradient(180deg, var(--nav-bottom) 0%, var(--nav-top) 100%);
    color: var(--white); text-align: center;
    font-size: 13px; line-height: 17px; letter-spacing: 0.6px;
    padding-top: 14px;
  }
</style>
</head>
<body>
<div class="page">
  <header class="hero" role="img" aria-label="Soft-focus photograph of medical staff at a desk with a stethoscope in the foreground">
    <div class="brand-mark"></div>
    <div class="brand-name">SKYVELLO MEDLIFT</div>
  </header>

  <nav class="main-nav">
    <span>ABOUT</span><span class="sep">|</span>
    <span>CONSULTANCY</span><span class="sep">|</span>
    <span>SERVICES</span><span class="sep">|</span>
    <span>CASE STUDIES</span><span class="sep">|</span>
    <span>EXAMPLE COSTS</span><span class="sep">|</span>
    <span>NEWS</span><span class="sep">|</span>
    <span>CONTACT</span>
  </nav>

  <div class="content-panel"><div class="content-strip"></div></div>

  <div class="social-links" aria-label="Social media links">
    <span style="left:0"></span>
    <span style="left:49px"></span>
    <span style="left:104px"></span>
    <span style="left:160px"></span>
  </div>

  <h1 class="page-title">ABOUT</h1>

  <div class="column column-left">
    <p>Our Medevac Service was originally part of our Private Charter service offered by our Sister company Jetvia</p>
    <p>Like most private charter brokers we offered a service based around the basic disciplines of standard charter projects. Seeking availability, calculating positioning costs, appropriate airports and type tested crew were all the basic challenges of providing an excellent service in the private charter world. However, as our Medevac service grew, and we started to grow a reputation for being excellent in this field, it seemed only logical that we should separate the two disciplines. It was obvious to us that whilst all of the disciplines mentioned above were important, the extra layer of knowledge and experience required to properly support a service that could be as basic as organising a comfortable flight or as complicated as a multi-aircraft trans continental service, with multiple flight crews and medical teams, required us to invest in ourselves first.</p>
    <p>The training and professional development of our teams has helped us create one of the UKs leading Consultancy services for any movement of a</p>
  </div>

  <div class="column column-right">
    <p>individual, or group of people, that involves aircraft and medical support.</p>
    <p>As a Consultancy we do not own the aircraft, nor do we employ the flight crew or airbourne medical teams. This means we can maintain total focus on the Patient. We are not distracted by worrying about paying for an expensive fleet of aircraft, paying for staff when they are not being used and clearly have no conflicts of interest when it comes to selecting the most appropriate method of support. We have one concern, &nbsp;the Patient.</p>
    <p>We seek the best aircraft, flight crew, medical team and price for our Clients, quickly, efficiently and transparently. We have a global reach and utilise helicopters, small light aircraft, commercial carriers and private air ambulances. Whatever is right for the Patient is right for us.</p>
    <p>We provide our services to individuals, businesses, Public Health Trusts, insurance companies and private clinics. We are proud of what we do, and hope that you will be too.</p>
  </div>

  <footer class="site-footer">
    <div>SVML</div>
    <div>Quillmere Orvanta Ltd</div>
    <div>Harwick, Westshire, United Kingdom, HW1 2AB</div>
    <div>+44 (0)200 000 0123</div>
    <div>operations@svml.example</div>
  </footer>
</div>
</body>
</html>
```